Update Powerpoint Presentation

We need to update the existing Powerpoint presentation to make it look more professional, less words and get the message across to potential clients. Our clients are banks and lenders in Australia.
Reason: To give the designers more time to come up with designs
Reason: I am looking for a design that is more innovative and doesn't just re-create what I gave. This presentation is only an example of what I would like I am keen to find a presentation that takes it to the next level.

```html
<!DOCTYPE html>
<html lang="en">
<head>
<meta charset="utf-8">
<title>Harbour Lending Services – Presentation Overview</title>
<link href="https://fonts.googleapis.com/css2?family=Carlito:wght@400;700&display=swap" rel="stylesheet">
<style>
:root{
  --bg-top:#2f3236;
  --bg-bottom:#5a5e63;
  --slide-light:#fdfdfd;
  --slide-dark:#d6d9dc;
  --navy:#15315a;
  --blue:#1f5fa6;
  --orange:#f39a1e;
  --tab-red:#a3191b;
  --icon-grey:#5d6b76;
  --ink:#333a40;
  --green-lime:#9bc34a;
  --green:#4cbb5e;
  --steel:#4a82a8;
  --purple:#7d55a8;
}
*{box-sizing:border-box;margin:0;padding:0}
html,body{width:1200px;height:768px;overflow:hidden}
body{
  background:linear-gradient(180deg,var(--bg-top),var(--bg-bottom));
  font-family:"Carlito",Calibri,Arial,sans-serif;
  position:relative;
}
.slide{
  position:absolute;width:318px;height:240px;
  background:linear-gradient(160deg,var(--slide-light) 30%,var(--slide-dark));
  overflow:hidden;
  box-shadow:0 2px 6px rgba(0,0,0,.4);
}
.tab{position:absolute;top:0;right:8px;width:15px;height:15px;background:var(--tab-red);border-radius:0 0 2px 2px}
.footer{
  position:absolute;left:0;bottom:0;width:100%;height:10px;background:var(--navy);
  color:#fff;font-size:6.5px;font-weight:700;text-align:center;line-height:10px;
}
.footer::before,.footer::after{
  content:"";position:absolute;top:1.5px;width:7px;height:7px;border-radius:50%;background:#8a96a3;
}
.footer::before{left:5px}
.footer::after{right:5px}
.slide-title{position:absolute;font-weight:700;color:var(--blue);font-size:8.5px}
.center-label{position:absolute;color:var(--blue);font-weight:700;font-size:9.5px}
.icon{position:absolute;left:0;top:0}
.placeholder{position:absolute}

/* cover */
.cover-map{left:14px;top:14px;width:288px;height:130px;border-radius:30px;
  background:radial-gradient(ellipse at 50% 45%,rgba(74,140,200,.85) 0%,rgba(90,155,210,.6) 50%,rgba(255,255,255,0) 78%)}
.cover-tagline{position:absolute;left:9px;top:180px;font-size:11px;font-weight:700;color:var(--blue)}
.cover-tagline span{color:var(--orange)}
.cover-brand{position:absolute;right:18px;top:184px;color:#fff;font-size:28px;font-weight:700;letter-spacing:1px}
.cover-brand-sub{position:absolute;right:18px;top:214px;color:#fff;font-size:6.5px}
.page-no{position:absolute;right:6px;bottom:8px;color:#fff;font-size:5px}

/* intro */
.intro-head{left:12px;top:17px;font-size:6.5px;text-transform:uppercase;border-bottom:1px solid var(--blue);width:270px;padding-bottom:2px}
.intro-text{position:absolute;left:80px;top:46px;width:228px;font-size:5.6px;line-height:1.32;color:var(--ink)}
.intro-text p{margin-bottom:4px}

.hand-icon{left:18px;top:80px;width:142px;height:62px;border-radius:8px;
  background:linear-gradient(90deg,rgba(93,107,118,.25),rgba(93,107,118,.45) 50%,rgba(93,107,118,.25))}

.goal-list{position:absolute;left:46px;top:38px}
.goal{position:relative;height:34px;margin-bottom:6px;width:236px}
.goal-box{position:absolute;left:0;top:0;width:96px;height:34px;border-radius:4px;color:#fff;font-weight:700;font-size:10px;text-align:center;line-height:34px;box-shadow:0 1px 2px rgba(0,0,0,.3)}
.goal-arrow{position:absolute;left:96px;top:3px;width:140px;height:28px;clip-path:polygon(0 0,88% 0,100% 50%,88% 100%,0 100%);
  font-size:4.8px;font-weight:700;color:var(--ink);padding:4px 20px 0 5px;line-height:1.25}
.financial .goal-box{background:var(--green-lime)} .financial .goal-arrow{background:#e3eed0}
.client .goal-box{background:var(--green)} .client .goal-arrow{background:#d5eedb}
.valueadd .goal-box{background:var(--steel)} .valueadd .goal-arrow{background:#d2e0ea}
.people .goal-box{background:var(--purple)} .people .goal-arrow{background:#e2d9ec}

.client-group{position:absolute;left:18px;width:72px;height:72px;border-radius:50%;border:9px solid var(--icon-grey);
  display:flex;align-items:center;justify-content:center;font-size:9px;font-weight:700;color:var(--blue)}
.brand-grid{position:absolute;display:grid;grid-template-columns:repeat(4,auto);gap:0 10px;grid-auto-rows:31px;
  font-size:8px;font-weight:700;color:var(--navy);align-items:center}
.brand-grid span{white-space:nowrap}
</style>
</head>
<body>

<!-- Row 1 -->
<section class="slide" style="left:116px;top:22px">
  <div class="placeholder cover-map" role="img" aria-label="World map with connection lines between office locations"></div>
  <svg width="318" height="240" class="icon">
    <path d="M0 240 L0 215 C90 210 170 150 318 150 L318 240 Z" fill="#15315a"/>
    <path d="M0 212 C90 207 170 148 318 146" stroke="#3b7dc4" stroke-width="2" fill="none"/>
  </svg>
  <div class="cover-tagline">Global Reach. <span>Local Touch.</span></div>
  <div class="cover-brand">HLS</div>
  <div class="cover-brand-sub">Global reach. Local touch.</div>
  <div class="page-no">1</div>
</section>

<section class="slide" style="left:450px;top:22px">
  <div class="tab"></div>
  <div class="slide-title intro-head">Introduction</div>
  <svg width="318" height="240" class="icon" role="img" aria-label="Information icon">
    <defs><linearGradient id="infoGrad" x1="0" y1="0" x2="1" y2="1"><stop offset="0" stop-color="#5cc8ee"/><stop offset="1" stop-color="#1c7fc0"/></linearGradient></defs>
    <path d="M41 74 A31 31 0 1 1 72 105 L72 136 L41 136 A31 31 0 0 1 10 105 A31 31 0 0 1 41 74 Z" fill="url(#infoGrad)" transform="translate(0 -2)"/>
    <circle cx="45" cy="88" r="5" fill="#fff"/>
    <rect x="40" y="97" width="9" height="26" rx="3" fill="#fff"/>
  </svg>
  <div class="intro-text">
    <p>Harbour Lending Services (HLS) was established in NZ in 2001 and opened an office in Australia in 2004. In November 2007 HLS became a wholly owned subsidiary of Northgate Financial Group and is the vehicle through which Northgate undertakes mortgage servicing in Australia and New Zealand.</p>
    <p>On 1 August 2012 HLS acquired Coastal Lenders Settlement Services (CLSS) to form one of the largest mortgage processing companies in Australasia.</p>
    <p>In providing services to the mortgage industry, HLS utilises and deploys its existing resources and capability as well as the resources available to it through the Northgate family of companies internationally.</p>
    <p>HLS have approximately 300 staff operating in offices in Sydney, Melbourne, Adelaide, Brisbane, Perth and Auckland, refer map opposite.</p>
    <p>HLS undertakes approximately 150,000 settlements p.a.</p>
  </div>
  <div class="footer">Website: www.harbourls.com &nbsp;|&nbsp; E-mail: info@harbourls.com</div>
</section>

<section class="slide" style="left:786px;top:22px">
  <div class="tab"></div>
  <svg width="318" height="240" class="icon" role="img" aria-label="Gears icon">
    <g transform="translate(62 118)" fill="#5d6b76">
      <circle r="30"/>
      <g>
        <rect x="-7" y="-40" width="14" height="14" rx="2"/>
        <rect x="-7" y="-40" width="14" height="14" rx="2" transform="rotate(45)"/>
        <rect x="-7" y="-40" width="14" height="14" rx="2" transform="rotate(90)"/>
        <rect x="-7" y="-40" width="14" height="14" rx="2" transform="rotate(135)"/>
        <rect x="-7" y="-40" width="14" height="14" rx="2" transform="rotate(180)"/>
        <rect x="-7" y="-40" width="14" height="14" rx="2" transform="rotate(225)"/>
        <rect x="-7" y="-40" width="14" height="14" rx="2" transform="rotate(270)"/>
        <rect x="-7" y="-40" width="14" height="14" rx="2" transform="rotate(315)"/>
      </g>
      <circle r="12" fill="#eef0f1"/>
    </g>
    <g transform="translate(102 86)" fill="#5d6b76">
      <circle r="13"/>
      <rect x="-3.5" y="-18" width="7" height="7" rx="1"/>
      <rect x="-3.5" y="-18" width="7" height="7" rx="1" transform="rotate(45)"/>
      <rect x="-3.5" y="-18" width="7" height="7" rx="1" transform="rotate(90)"/>
      <rect x="-3.5" y="-18" width="7" height="7" rx="1" transform="rotate(135)"/>
      <rect x="-3.5" y="-18" width="7" height="7" rx="1" transform="rotate(180)"/>
      <rect x="-3.5" y="-18" width="7" height="7" rx="1" transform="rotate(225)"/>
      <rect x="-3.5" y="-18" width="7" height="7" rx="1" transform="rotate(270)"/>
      <rect x="-3.5" y="-18" width="7" height="7" rx="1" transform="rotate(315)"/>
      <circle r="5" fill="#f1f2f3"/>
    </g>
  </svg>
  <div class="center-label" style="left:180px;top:112px">Service Offerings</div>
  <div class="footer">Website: www.harbourls.com &nbsp;|&nbsp; E-mail: info@harbourls.com</div>
</section>

<!-- Row 2 -->
<section class="slide" style="left:116px;top:270px">
  <div class="tab"></div>
  <svg width="318" height="240" class="icon" role="img" aria-label="Connected nodes icon">
    <g stroke="#5d6b76" stroke-linecap="round">
      <line x1="52" y1="128" x2="46" y2="84" stroke-width="9"/>
      <line x1="52" y1="128" x2="78" y2="94" stroke-width="9"/>
      <circle cx="40" cy="80" r="10" fill="#f6f7f7" stroke-width="8"/>
      <circle cx="80" cy="92" r="10" fill="#f6f7f7" stroke-width="8"/>
    </g>
    <circle cx="54" cy="130" r="25" fill="#5d6b76"/>
  </svg>
  <div class="center-label" style="left:166px;top:108px">Stratergic Framework</div>
  <div class="footer">Website: www.harbourls.com &nbsp;|&nbsp; E-mail: info@harbourls.com</div>
</section>

<section class="slide" style="left:450px;top:270px">
  <div class="tab"></div>
  <div class="slide-title" style="left:14px;top:10px">Our Vision :</div>
  <svg width="318" height="240" class="icon" font-family="Carlito, sans-serif" font-size="7.5" font-weight="700" fill="#fff" text-anchor="middle">
    <g transform="translate(162 107)" stroke="#fff" stroke-width="2">
      <path d="M0 0 L0 -75 A75 75 0 0 1 71.33 -23.18 Z" fill="#d9383a"/>
      <path d="M0 0 L71.33 -23.18 A75 75 0 0 1 44.08 60.68 Z" fill="#8cc43f"/>
      <path d="M0 0 L44.08 60.68 A75 75 0 0 1 -44.08 60.68 Z" fill="#7d4fa8"/>
      <path d="M0 0 L-44.08 60.68 A75 75 0 0 1 -71.33 -23.18 Z" fill="#3bb6d3"/>
      <path d="M0 0 L-71.33 -23.18 A75 75 0 0 1 0 -75 Z" fill="#f39a2b"/>
      <g stroke="none">
        <text x="26" y="-34">People</text>
        <text x="43" y="16">Tools</text>
        <text x="0" y="47">Processes</text>
        <text x="-43" y="16">Innovation</text>
        <text x="-26" y="-34">Solution</text>
      </g>
    </g>
  </svg>
  <div class="center-label" style="left:0;width:318px;text-align:center;top:205px;font-size:7.5px">Better Than Everyone Else</div>
  <div class="footer">Website: www.harbourls.com &nbsp;|&nbsp; E-mail: info@harbourls.com</div>
</section>

<section class="slide" style="left:786px;top:270px">
  <div class="tab"></div>
  <div class="slide-title" style="left:14px;top:10px">Values:</div>
  <svg width="318" height="240" class="icon" font-family="Carlito, sans-serif" font-size="7.5" font-weight="700" fill="#fff" text-anchor="middle">
    <g transform="translate(166 102)" stroke="#fff" stroke-width="3">
      <path d="M0 0 L-75 0 A75 75 0 0 1 0 -75 Z" fill="#7b5ea7"/>
      <path d="M0 0 L0 -75 A75 75 0 0 1 75 0 Z" fill="#5a4fa6"/>
      <path d="M0 0 L-75 0 A75 75 0 0 0 0 75 Z" fill="#3fb8d8"/>
      <path d="M0 0 L75 0 A75 75 0 0 1 0 75 Z" fill="#3c6fc5"/>
      <circle r="8" fill="none" stroke="#fff" stroke-width="2.5"/>
      <g stroke="none">
        <text x="-28" y="-26">Teamwork</text>
        <text x="28" y="-26">Ownership</text>
        <text x="-28" y="30">Consistency</text>
        <text x="28" y="30">Authentic</text>
      </g>
    </g>
  </svg>
  <div class="footer">Website: www.harbourls.com &nbsp;|&nbsp; E-mail: info@harbourls.com</div>
</section>

<!-- Row 3 -->
<section class="slide" style="left:116px;top:517px">
  <div class="tab"></div>
  <div class="slide-title" style="left:12px;top:10px">Goals and measures of success:</div>
  <div class="goal-list">
    <div class="goal financial"><div class="goal-box">Financial</div><div class="goal-arrow">• Profitability through revenue growth, margin and cost management and operational efficiencies.</div></div>
    <div class="goal client"><div class="goal-box">Client</div><div class="goal-arrow">• Increase our share and breadth of services. Cross sell of other services.</div></div>
    <div class="goal valueadd"><div class="goal-box">Value Add</div><div class="goal-arrow">• Delivering innovative solutions that enhance our customers capabilities.</div></div>
    <div class="goal people"><div class="goal-box">People</div><div class="goal-arrow">• Building an agile and resilient workforce with people empowered to reach their full potential</div></div>
  </div>
  <div class="footer">Website: www.harbourls.com &nbsp;|&nbsp; E-mail: info@harbourls.com</div>
</section>

<section class="slide" style="left:450px;top:517px">
  <div class="tab"></div>
  <div class="placeholder hand-icon" role="img" aria-label="Handshake illustration in slate grey"></div>
  <div class="center-label" style="left:192px;top:98px">Key Existing Clients</div>
  <div class="footer">Website: www.harbourls.com &nbsp;|&nbsp; E-mail: info@harbourls.com</div>
</section>

<section class="slide" style="left:786px;top:517px">
  <div class="tab"></div>
  <div class="client-group" style="top:24px">Banks</div>
  <div class="client-group" style="top:120px">Non-Banks</div>
  <div class="brand-grid" style="left:110px;top:17px">
    <span>Ridgeway Bank</span><span>Orbis</span><span>Kestrel</span><span>Onyx</span>
    <span>Nexa</span><span>Nexa Broker</span><span>Sunvale</span><span>Member Bank</span>
    <span>Halden</span><span>Upland Bank</span><span>Fernbank</span><span>Edgeline</span>
  </div>
  <div class="brand-grid" style="left:110px;top:122px">
    <span>Redstone</span><span>Pickfund</span><span>Southerly</span><span>Alder Group</span>
    <span>Blueprint Loans</span><span>Ravensby</span><span>Libra Finance</span><span>Resivale</span>
    <span>Quicklend</span><span>Watchpoint</span><span>Ardent</span>
  </div>
  <div class="footer">Website: www.harbourls.com &nbsp;|&nbsp; E-mail: info@harbourls.com</div>
</section>

</body>
</html>
```